Post Card (5x7) - Pre-foreclosure Image - Harbor Path Partners

(Two-Sided Post Card)
FACING FORECLOSURE? YOU STILL HAVE OPTIONS.
If you’re behind on payments or at risk of foreclosure, you’re not alone—and it’s not too late to take action.
We help homeowners:
• Explore options to stay in their home
• Stop or delay foreclosure
• Sell quickly for a fair price if needed
No pressure. No obligation. Just real solutions tailored to your situation.
Call - (240) 558-2094
Email - marcus@hpbllc-mail.com
Harbor Path Partners LLC
7200 Bramwick Lane, Fairhaven, MD 21987
**Marcus Fennimore is a Licensed Realtor with Copperleaf Homes Realty in Lakeby, Maryland.
(Leave room for mailing address, return address & postage)
Target Market(s)
Distressed Homeowners
Industry/Entity Type
Real Estate

```html
<!DOCTYPE html>
<html lang="en">
<head>
<meta charset="utf-8">
<title>Harbor Path Partners – Pre-foreclosure Postcard</title>
<link href="https://fonts.googleapis.com/css2?family=Bebas+Neue&family=Montserrat:wght@400;500;600&display=swap" rel="stylesheet">
<style>
  :root {
    --ink: #000000;
    --paper: #ffffff;
    --rule: #222222;
    --sky-top: #3a4152;
    --sky-mid: #c98a3e;
    --sun: #f2b44a;
    --water: #2a1e14;
  }
  * { margin: 0; padding: 0; box-sizing: border-box; }
  html, body { width: 1200px; height: 1200px; overflow: hidden; background: var(--paper); }
  body { position: relative; font-family: "Montserrat", sans-serif; color: var(--ink); }

  .card { position: absolute; top: 447px; width: 432px; height: 308px; overflow: hidden; }
  .card--front { left: 144px; }
  .card--back { left: 638px; border: 2px solid var(--rule); background: var(--paper); }

  .scene-photo {
    position: absolute; inset: 0;
    background:
      radial-gradient(circle at 72% 50%, var(--sun) 0, rgba(242,180,74,0.6) 12%, rgba(201,138,62,0) 35%),
      linear-gradient(180deg, var(--sky-top) 0%, #6f6a6a 25%, var(--sky-mid) 50%, #3b2a1c 68%, var(--water) 100%);
  }
  .chevron { position: absolute; inset: 0; width: 100%; height: 100%; }

  .front-copy { position: absolute; left: 9px; top: 12px; color: var(--paper); }
  .headline { font-family: "Bebas Neue", sans-serif; font-size: 43px; line-height: 44px; font-weight: 400; letter-spacing: 0.2px; }
  .subhead { font-size: 16.5px; font-weight: 500; margin-top: 3px; letter-spacing: 0.2px; }
  .lede { font-size: 14.5px; line-height: 25.6px; margin-left: 3px; }

  .front-brand { position: absolute; left: 9px; bottom: 14px; display: flex; align-items: center; gap: 6px; color: var(--paper); font-size: 10px; font-weight: 600; white-space: nowrap; }
  .front-brand .mark { width: 12px; height: 12px; background: var(--paper); }

  .back-copy { position: absolute; left: 8px; top: 24px; color: var(--paper); font-size: 14.5px; line-height: 25.6px; width: 220px; }
  .back-copy .lead { font-weight: 600; }
  .back-copy .gap { height: 25.6px; }

  .brand-block { position: absolute; left: 256px; top: 46px; width: 160px; text-align: center; font-size: 12px; font-weight: 600; letter-spacing: 2px; line-height: 14px; white-space: nowrap; }
  .address-lines { position: absolute; left: 266px; top: 87px; width: 148px; }
  .address-lines span { display: block; height: 19.5px; border-bottom: 1px solid var(--rule); }
  .address-lines span:first-child { height: 1px; }

  .contact { position: absolute; left: 236px; top: 194px; font-size: 9.5px; line-height: 18px; white-space: nowrap; }
  .contact li { list-style: none; display: flex; align-items: center; gap: 4px; }
  .contact svg { width: 12px; height: 12px; flex: none; }

  .legal { position: absolute; left: 229px; font-size: 7px; line-height: 9.5px; border-left: 2px solid var(--ink); padding-left: 5px; white-space: nowrap; }
  .legal--office { top: 254px; }
  .legal--license { top: 281px; }
</style>
</head>
<body>
  <section class="card card--front">
    <div class="scene-photo" role="img" aria-label="City skyline silhouetted against a sunset over a river"></div>
    <svg class="chevron" viewBox="0 0 432 308" preserveAspectRatio="none" aria-hidden="true">
      <polygon points="0,0 179,0 268,154 179,308 0,308" fill="#000"/>
    </svg>
    <div class="front-copy">
      <h1 class="headline">FACING<br>FORECLOSURE?</h1>
      <p class="subhead">YOU STILL HAVE OPTIONS.</p>
      <p class="lede">If you’re behind on<br>payments or at risk of<br>foreclosure, you’re not<br>alone—and it’s not too late<br>to take action.</p>
    </div>
    <div class="front-brand"><span class="mark"></span>Harbor Path Partners</div>
  </section>

  <section class="card card--back">
    <svg class="chevron" viewBox="0 0 428 304" preserveAspectRatio="none" aria-hidden="true">
      <polygon points="0,0 176,0 266,152 176,304 0,304" fill="#000"/>
    </svg>
    <div class="back-copy">
      <p class="lead">We help homeowners:</p>
      <p>• Explore options to stay in<br>their home</p>
      <p>• Stop or delay foreclosure</p>
      <p>• Sell quickly for a fair price<br>if needed</p>
      <div class="gap"></div>
      <p>No pressure. No obligation.<br>Just real solutions tailored<br>to your situation.</p>
    </div>

    <div class="brand-block">HARBOR PATH<br>PARTNERS LLC</div>

    <div class="address-lines" aria-label="Mailing address area"><span></span><span></span><span></span><span></span><span></span></div>

    <ul class="contact">
      <li>
        <svg viewBox="0 0 24 24" aria-hidden="true"><path d="M6.6 10.8a15 15 0 0 0 6.6 6.6l2.2-2.2a1 1 0 0 1 1-.25 11.4 11.4 0 0 0 3.6.57 1 1 0 0 1 1 1V20a1 1 0 0 1-1 1A17 17 0 0 1 3 4a1 1 0 0 1 1-1h3.5a1 1 0 0 1 1 1c0 1.25.2 2.45.57 3.57a1 1 0 0 1-.25 1z" fill="#000"/></svg>
        Call - (240) 558-2094
      </li>
      <li>
        <svg viewBox="0 0 24 24" aria-hidden="true"><circle cx="12" cy="12" r="4" fill="none" stroke="#000" stroke-width="2.2"/><path d="M16 8v5a3 3 0 0 0 6 0v-1a10 10 0 1 0-4 8" fill="none" stroke="#000" stroke-width="2.2"/></svg>
        Email - marcus@hpbllc-mail.com
      </li>
    </ul>

    <p class="legal legal--office">Harbor Path Partners LLC<br>7200 Bramwick Lane, Fairhaven, MD 21987.</p>
    <p class="legal legal--license">Marcus Fennimore is a Licensed Realtor with<br>Copperleaf Homes Realty in Lakeby, Maryland</p>
  </section>
</body>
</html>
```